Re-design of Business Card

We require a design for our business card.

Korrim is a supplier of industrial packaging specializing in plastic products. We are undergoing a rebranding to appear more corporate. We have changed our company name to korrim and have a new logo.

I have uploaded our old card design with the previous company name.
Don't copy the current design. We are looking for a new design.

Industry/Entity Type

Manufacturing

Contact Information for Business Card

please don't copy the current design. we are looking for a new design.

Font styles to use
Sans Serif

Colors

Designer to choose colors to be used in the design.

Requirements
Must have
• clean and easy to read.

```html
<!DOCTYPE html>
<html lang="en">
<head>
<meta charset="utf-8">
<title>Korrim Business Card</title>
<link rel="stylesheet" href="https://fonts.googleapis.com/css2?family=Roboto:wght@400;700;900&display=swap">
<style>
  :root {
    --bg: #5e5e5e;
    --orange: #f07d1e;
    --dark: #222222;
    --map: #2e2622;
    --white: #ffffff;
    --ink: #4a4a4a;
    --rule: #8a8a8a;
  }
  * { margin: 0; padding: 0; box-sizing: border-box; }
  html, body { width: 1200px; height: 1200px; overflow: hidden; background: var(--bg); }
  body { font-family: 'Roboto', Arial, sans-serif; position: relative; }

  .card {
    position: absolute;
    left: 220px;
    width: 760px;
    height: 434px;
    box-shadow: 0 6px 18px rgba(0,0,0,.35);
  }
  .card-front { top: 120px; background: var(--dark); }
  .card-back { top: 630px; background: var(--white); }

  .front-map {
    position: absolute;
    left: 200px; top: 70px;
    width: 380px; height: 290px;
    background: var(--map);
    border-radius: 40% 45% 38% 50% / 45% 40% 55% 45%;
  }
  .brand {
    display: flex; align-items: center; gap: 14px;
    color: var(--orange);
    font-weight: 900;
    letter-spacing: 2px;
  }
  .brand-square { width: 0.55em; height: 0.55em; background: var(--orange); }
  .front-brand {
    position: absolute; left: 0; right: 0; top: 160px;
    justify-content: center; font-size: 96px;
  }
  .front-url {
    position: absolute; left: 0; right: 0; top: 330px;
    text-align: center; color: var(--white); font-size: 18px;
  }
  .front-url .accent { color: var(--orange); }

  .back-brand {
    position: absolute; left: 40px; top: 180px;
    font-size: 66px;
  }
  .back-rule {
    position: absolute; left: 372px; top: 70px;
    width: 1px; height: 300px; background: var(--rule);
  }
  .contact {
    position: absolute; left: 400px; top: 60px;
    color: var(--ink); font-size: 16px; line-height: 1.35;
  }
  .contact-name, .contact-heading {
    color: var(--orange); font-weight: 700; font-size: 22px; text-transform: uppercase;
  }
  .contact-role { margin-bottom: 8px; }
  .contact-heading { margin-top: 14px; }
  .row { display: flex; align-items: flex-start; gap: 8px; margin-top: 3px; }
  .row-gap { margin-top: 12px; }
  .icon {
    flex: none; width: 16px; height: 16px; margin-top: 2px;
    background: var(--orange); display: flex; align-items: center; justify-content: center;
  }
  .icon svg { width: 12px; height: 12px; }
</style>
</head>
<body>
  <section class="card card-front">
    <div class="front-map" role="img" aria-label="Faint map of Australia behind the name"></div>
    <div class="brand front-brand"><span class="brand-square"></span>KORRIM</div>
    <p class="front-url">www.<span class="accent">korrim</span>.com.au</p>
  </section>

  <section class="card card-back">
    <div class="brand back-brand"><span class="brand-square"></span>KORRIM</div>
    <div class="back-rule"></div>
    <div class="contact">
      <p class="contact-name">Daniel Brooks</p>
      <p class="contact-role">Machinery Sales Manager</p>
      <div class="row"><span class="icon"><svg viewBox="0 0 12 12"><path d="M2 1h3l1 3-2 1a6 6 0 0 0 3 3l1-2 3 1v3c-6 1-10-3-9-9z" fill="#fff"/></svg></span>XXXX XXX XXX</div>
      <div class="row"><span class="icon"><svg viewBox="0 0 12 12"><rect x="1" y="3" width="10" height="7" fill="none" stroke="#fff"/><path d="M1 3l5 4 5-4" fill="none" stroke="#fff"/></svg></span>daniel@korrim.com.au</div>
      <p class="contact-heading">Head Office</p>
      <div class="row"><span class="icon"><svg viewBox="0 0 12 12"><path d="M6 11S2 7 2 4.5a4 4 0 0 1 8 0C10 7 6 11 6 11z" fill="#fff"/><circle cx="6" cy="4.5" r="1.4" fill="#f07d1e"/></svg></span><span>14 Harwood St<br>Kelvin Park, Qld<br>4160 Australia</span></div>
      <div class="row row-gap"><span class="icon"><svg viewBox="0 0 12 12"><path d="M2 1h3l1 3-2 1a6 6 0 0 0 3 3l1-2 3 1v3c-6 1-10-3-9-9z" fill="#fff"/></svg></span>1300 418 327</div>
      <div class="row"><span class="icon"><svg viewBox="0 0 12 12"><rect x="2" y="5" width="8" height="5" fill="#fff"/><rect x="3" y="1" width="6" height="4" fill="none" stroke="#fff"/></svg></span>+61 7 3804 2157</div>
      <div class="row"><span class="icon"><svg viewBox="0 0 12 12"><circle cx="6" cy="6" r="4.5" fill="none" stroke="#fff"/><path d="M1.5 6h9M6 1.5c-2 2.5-2 6.5 0 9M6 1.5c2 2.5 2 6.5 0 9" fill="none" stroke="#fff" stroke-width=".8"/></svg></span>www.korrim.com.au</div>
    </div>
  </section>
</body>
</html>
```